KV Group

We need a new website for our company and since we had a very good work done for our logo in this site, we're back for the entire job.

Our company name is Marlowe Capital Group. We're adding files of examples of what we have done today. In my opinion we need a more attention lock in the site but yet financial simple work.

Our files (attached) will let you know what we have so far. We need a complete change but the colours should be the same, however you can change them not running away to far from the original, and of course matching with the logo.

We need examples for 3 kind of layouts.

- A HOME welcome layout
- An internal Layout with sidebar
- And internal Layout wide

We can buy image licenses if needed for assets.
Actually there are 5 slide images placed on the Welcome HOME, we need those there, but you can improve with better images to match the new website!!!

Target Market(s)

Clients looking for financial advisers, tax and funds specialist, currency advisers

Industry/Entity Type

Financial

Requirements
Must have
• all the fonts must be in accordance with the financial market sites........the welcome home page must be precise, neat and information accurate........the menu should be elegant........main focus on the Home page, should be also the PRIVATE ACCESS box log in.......

```html
<!DOCTYPE html>
<html lang="en">
<head>
<meta charset="utf-8">
<title>Marlowe Capital Group — Client Relations</title>
<link href="https://fonts.googleapis.com/css2?family=Cuprum:wght@400;700&display=swap" rel="stylesheet">
<style>
:root{
  --page:#eeebe5;
  --panel:#f8f6f2;
  --orange:#e8731d;
  --brown-dark:#3b1f08;
  --brown:#5a3312;
  --ink:#2f2f2f;
  --text:#4a4a4a;
  --rule:#cfcac2;
  --footer:#3c3c3c;
  --footer-base:#2e2e2e;
  --footer-link:#e6e6e6;
  --footer-dim:#6b6b6b;
}
*{margin:0;padding:0;box-sizing:border-box}
html,body{width:941px;height:1200px;overflow:hidden}
body{background:var(--page);font-family:"Cuprum",sans-serif;color:var(--text);position:relative}
a{color:inherit;text-decoration:none}
.top-line{position:absolute;left:0;top:0;width:941px;height:3px;background:var(--brown-dark)}
.quick-links{position:absolute;left:669px;top:0;width:190px;height:35px;background:var(--brown-dark);border-radius:0 0 6px 6px;display:flex;align-items:center;justify-content:space-around;color:#fff;font-size:14px}
.quick-links span{display:flex;align-items:center;gap:6px}
.brand{position:absolute;left:83px;top:40px;display:flex;align-items:center;gap:9px;color:var(--ink);font-size:19px;font-weight:700;letter-spacing:.3px}
.brand-mark{width:20px;height:20px;background:var(--orange)}
.main-nav{position:absolute;left:327px;top:57px;display:flex;align-items:center;font-size:14px;color:var(--ink)}
.main-nav a{padding:0 17px;line-height:26px;position:relative}
.main-nav a+a::before{content:"";position:absolute;left:0;top:9px;width:1px;height:9px;background:var(--ink)}
.main-nav a.active{background:var(--orange);color:#fff;padding:0 16px;border-radius:1px}
.main-nav a.active+a::before{display:none}
.main-nav a:last-child{padding-right:0}
.header-rule{position:absolute;left:83px;top:96px;width:776px;height:1px;background:var(--rule)}
.hero{position:absolute;left:83px;top:113px;width:550px;height:207px;background:linear-gradient(135deg,#f7e3a1 0%,#e3a93a 45%,#b8741a 75%,#f3d487 100%)}
.login{position:absolute;left:649px;top:113px;width:210px;height:207px;background:linear-gradient(180deg,#5c320f,#3e1f07);padding:10px 15px;color:#fff}
.login h2{font-size:16px;font-weight:400;margin-bottom:9px}
.login label{display:block;font-size:11px;margin-bottom:3px}
.login .field{height:28px;background:#fff;margin-bottom:12px}
.login .forgot{font-size:11px;display:block;margin-top:4px}
.login .btn{position:absolute;right:14px;bottom:16px;background:#2a1404;font-size:12px;padding:4px 12px}
.crumbs{position:absolute;left:83px;top:334px;font-size:11px;color:var(--ink)}
.crumbs a{color:var(--orange);text-decoration:underline}
.content-panel{position:absolute;left:83px;top:360px;width:776px;height:537px;background:var(--panel)}
.article{position:absolute;left:96px;top:373px;width:534px;font-size:11.2px;line-height:17.6px}
.article h1{font-size:24px;font-weight:400;color:var(--ink);margin-bottom:2px}
.article h2{font-size:17px;font-weight:400;color:var(--orange);margin:14px 0 8px}
.article p+p{margin-top:17px}
.sidebar{position:absolute;left:650px;top:372px;width:195px}
.sidebar h3{font-size:15px;font-weight:400;color:var(--ink);margin-bottom:2px}
.sidebar .thumb{width:194px;height:63px;border:1px solid #c9c4bc;margin-bottom:5px}
.sidebar p{font-size:9.6px;line-height:13px;margin-bottom:18px;color:var(--ink)}
.t1{background:linear-gradient(120deg,#f4f4f2,#cfd6dc 60%,#8e97a0)}
.t2{background:linear-gradient(120deg,#2c3440,#8e949c 50%,#e8e6e2)}
.t3{background:linear-gradient(180deg,#7fb0d8 0%,#a9c9e0 45%,#3f6b3a 75%,#274a25)}
.badges{display:flex;gap:16px;align-items:center;margin-top:14px}
.badge{width:38px;height:20px;border:1px solid #9aa;border-radius:3px;background:#fff}
.badge.round{width:26px;height:26px;border-radius:50%;background:#1f3d6e;border:2px solid var(--orange)}
.site-footer{position:absolute;left:0;top:917px;width:941px;height:230px;background:var(--footer)}
.fcol{position:absolute;top:929px}
.fcol h4{font-size:19px;font-weight:400;color:var(--orange);margin-bottom:10px}
.fcol li{list-style:none;font-size:11.5px;line-height:15.6px;color:var(--footer-link)}
.footer-base{position:absolute;left:0;top:1147px;width:941px;height:53px;background:var(--footer-base)}
.copyright{position:absolute;left:83px;top:1166px;font-size:9px;color:var(--footer-dim);font-family:Arial,sans-serif}
.base-note{position:absolute;left:325px;top:1154px;width:533px;font-size:9px;line-height:12px;color:#5a5a5a;text-align:right}
</style>
</head>
<body>
<div class="top-line"></div>
<nav class="quick-links">
  <span><svg width="16" height="14" viewBox="0 0 16 14"><path d="M2 2h12v9H2z" fill="none" stroke="#fff" stroke-width="1.5"/><path d="M5 7l2 2 4-4" fill="none" stroke="#fff" stroke-width="1.5"/></svg>Apply Now</span>
  <span><svg width="16" height="12" viewBox="0 0 16 12"><path d="M1 1h14v10H1z" fill="none" stroke="#fff" stroke-width="1.5"/><path d="M1 1l7 6 7-6" fill="none" stroke="#fff" stroke-width="1.5"/></svg>Contact us</span>
</nav>
<div class="brand"><span class="brand-mark"></span>Marlowe Capital Group</div>
<nav class="main-nav">
  <a class="active">Home</a><a>About us</a><a>Investments</a><a>Funds</a><a>Brokerage</a><a>Exchange</a><a>Accounts</a>
</nav>
<div class="header-rule"></div>

<div class="hero" role="img" aria-label="Golden dollar signs over a financial grid"></div>
<form class="login">
  <h2>Private Access</h2>
  <label>User Name:</label><div class="field"></div>
  <label>Password:</label><div class="field"></div>
  <span class="forgot">Forgot password</span>
  <span class="btn">Read More</span>
</form>

<div class="crumbs"><a>Home</a> &gt; <a>Investment</a> &gt; Client relations</div>
<div class="content-panel"></div>

<article class="article">
  <h1>Client Relations</h1>
  <p>Lorem Ipsum is simply dummy text of the printing and typesetting industry. Lorem Ipsum has been the industry's standard dummy text ever since the 1500s, when an unknown printer took a galley of type and scrambled it to make a type specimen book. It has survived not only five centuries, but also the leap into electronic typesetting, remaining essentially unchanged. It was popularised in the 1960s with the release of Letraset sheets containing Lorem Ipsum passages, and more recently with desktop publishing software like Aldus PageMaker including versions of Lorem Ipsum.</p>
  <h2>You needs and requirments</h2>
  <p>Lorem Ipsum is simply dummy text of the printing and typesetting industry. Lorem Ipsum has been the industry's standard dummy text ever since the 1500s, when an unknown printer took a galley of type and scrambled it to make a type specimen book. It has survived not only five centuries.</p>
  <p>But also the leap into electronic typesetting, remaining essentially unchanged. It was popularised in the 1960s with the release of Letraset sheets containing Lorem Ipsum passages, and more recently with desktop publishing software like Aldus PageMaker including versions of Lorem Ipsum.</p>
  <h2>A truly personal relationship</h2>
  <p>Lorem Ipsum is simply dummy text of the printing and typesetting industry. Lorem Ipsum has been the industry's standard dummy text ever since the 1500s, when an unknown printer took a galley of type and scrambled it to make a type specimen book. It has survived not only five centuries.</p>
  <p>But also the leap into electronic typesetting, remaining essentially unchanged. It was popularised in the 1960s with the release of Letraset sheets containing Lorem Ipsum passages, and more recently with desktop publishing software like Aldus PageMaker including versions of Lorem Ipsum.</p>
</article>

<aside class="sidebar">
  <h3>Management &amp; Stratery</h3>
  <div class="thumb t1" role="img" aria-label="Hands reviewing charts with a pen"></div>
  <p>Lorem Ipsum is simply dummy text of the printing and typesetting industry. Lorem Ipsum has been the industry's standard dummy text ever</p>
  <h3>Funds</h3>
  <div class="thumb t2" role="img" aria-label="Business handshake"></div>
  <p>Lorem Ipsum is simply dummy text of the printing and typesetting industry. Lorem Ipsum has been the industry's standard dummy text ever</p>
  <h3>Currency Exchange</h3>
  <div class="thumb t3" role="img" aria-label="City towers behind palm trees"></div>
  <p>Lorem Ipsum is simply dummy text of the printing and typesetting industry. Lorem Ipsum has been the industry's standard dummy text ever</p>
  <h3>Verified and Protected by</h3>
  <div class="badges"><span class="badge"></span><span class="badge"></span><span class="badge"></span><span class="badge round"></span></div>
</aside>

<footer class="site-footer"></footer>
<div class="fcol" style="left:83px"><h4>About us</h4><ul><li>History</li><li>Expertize</li><li>Identity</li><li>Strartegy</li><li>Contact us</li></ul></div>
<div class="fcol" style="left:217px"><h4>Investments</h4><ul><li>Term Deposits</li><li>managment &amp; Strategy</li><li>Client Relations</li><li>Financial Privacy</li><li>Tax Advice</li><li>Wealth Analysis &amp; Financial Planning</li><li>Active Advisory Group</li><li>Manager Selection Services</li><li>Private Equity</li></ul></div>
<div class="fcol" style="left:403px"><h4>Currency Exchange</h4><ul><li>Overview</li><li>Administration</li><li>Funds Security</li><li>Core Services</li><li>Reporting</li><li>Revenue oprtunities</li><li>How it works?</li><li>Glossary</li></ul></div>
<div class="fcol" style="left:563px"><h4>Funds</h4><ul><li>Foreign Exchange</li><li>Fx Forward</li><li>Fx Options</li></ul></div>
<div class="fcol" style="left:563px;top:1035px"><h4>Brokerage</h4><ul><li>Institutional</li><li>Research</li><li>Trading</li></ul></div>
<div class="fcol" style="left:721px"><h4>Accounts</h4><ul><li>Apply Now</li><li>Private Access</li></ul></div>
<div class="footer-base"></div>
<div class="copyright">© Copyright websitename . All Rights Reserved</div>
<p class="base-note">Lorem Ipsum is simply dummy text of the printing and typesetting industry. Lorem Ipsum has been the industry's standard dummy text ever since the 1500s, when an unknown printer took a galley of type and scrambled it to make a type specimen book. It has survived not only five centuries, but also the leap into electronic typesetting, remaining essentially unchanged. It was popularised in the 1960s with</p>
</body>
</html>
```